Postcard for Educational Consultant
Lingua Bridge Learning Partners
Bridging Languages with Technology
Education
Public schools, private and charter schools, school districts
My logo. Please match colors to it.
Instructions for postcard text.
Photo 1
Photo 2 (purchased from PixVault)
Photo 3 (purchased from PixVault)
Photo 4 (purchased from PixVault)
QR Code
Photo 4

```html
<!DOCTYPE html>
<html lang="en">
<head>
<meta charset="utf-8">
<title>Lingua Bridge Learning Partners – Postcard</title>
<link href="https://fonts.googleapis.com/css2?family=Source+Sans+3:ital,wght@0,400;0,600;0,700;1,600;1,700&display=swap" rel="stylesheet">
<style>
  :root{
    --stage:#e9e6e1;
    --paper:#ffffff;
    --teal:#1b8fae;
    --blue:#1f9fcd;
    --deep:#166f88;
    --ink:#4d6a7a;
    --accent:#2a9bbd;
    --green:#8cc63f;
    --photo-warm:#c9a58a;
    --photo-pink:#e5a6b8;
    --photo-room:#6c5a4c;
    --photo-green:#7fa870;
  }
  *{box-sizing:border-box;margin:0;padding:0}
  html,body{width:1200px;height:850px;overflow:hidden}
  body{background:var(--stage);position:relative;font-family:"Source Sans 3",Arial,sans-serif}
  .card{position:absolute;width:540px;height:382px;background:var(--paper);overflow:hidden;box-shadow:0 6px 18px rgba(0,0,0,.25)}
  .card--front{left:30px;top:420px}
  .card--back{left:630px;top:40px}

  /* front */
  .front-photo{position:absolute;right:0;top:0;width:235px;height:300px;background:linear-gradient(160deg,var(--photo-room),var(--photo-warm) 55%,var(--photo-pink))}
  .front-copy{position:absolute;left:20px;top:24px;width:270px;color:var(--ink);font-size:12px;line-height:1.3}
  .front-copy .intro{margin-bottom:8px}
  .front-copy .hook{color:var(--accent);font-weight:700;font-style:italic;font-size:13px;line-height:1.25;margin-bottom:8px}
  .bullets{list-style:none}
  .bullets li{position:relative;padding-left:11px;margin-bottom:3px;color:var(--accent);font-size:11px;line-height:1.25}
  .bullets li::before{content:"•";position:absolute;left:0}
  .bullets .shout{font-weight:700;text-transform:uppercase}
  .front-band{position:absolute;left:0;bottom:0;width:100%;height:82px;background:var(--teal);display:flex;align-items:center;padding:0 20px;color:#fff}
  .brand{display:flex;align-items:center;gap:8px;font-size:12px;line-height:1.15;font-weight:600}
  .brand__dot{width:26px;height:26px;border-radius:50%;background:var(--green);flex:none}
  .front-band .brand{width:200px}
  .contact{margin-left:auto;margin-right:20px;font-size:11px;line-height:1.35;text-align:left}
  .contact strong{font-size:15px;font-weight:700}

  /* back */
  .back-photo-group{position:absolute;left:0;top:0;width:245px;height:120px;background:linear-gradient(120deg,#3b3531,var(--photo-warm) 45%,#4a5b6b)}
  .back-photo-boy{position:absolute;right:0;top:0;width:295px;height:300px;background:linear-gradient(200deg,#e9eef0,var(--photo-warm) 50%,var(--photo-green))}
  .back-title{position:absolute;left:110px;top:20px;color:#fff;font-style:italic;font-weight:700;font-size:21px;line-height:1.05;text-shadow:0 1px 3px rgba(0,0,0,.6);width:200px}
  .back-panel{position:absolute;left:0;top:120px;width:245px;height:262px;background:var(--blue);color:#fff;padding:12px 12px 0 14px;font-size:9.4px;line-height:1.28}
  .back-panel p{margin-bottom:7px}
  .back-panel .bullets li{color:#fff;font-size:9.4px;margin-bottom:1px;padding-left:9px}
  .back-foot{position:absolute;left:245px;bottom:0;width:295px;height:82px;background:var(--paper);padding:12px 14px}
  .back-foot .brand{color:var(--teal)}
  .web{position:absolute;left:14px;bottom:10px;color:var(--deep);font-size:12.5px;line-height:1.2}
  .web strong{display:block;font-size:14px;font-weight:700}
</style>
</head>
<body>

<section class="card card--back" aria-label="Postcard back">
  <div class="back-photo-group" role="img" aria-label="Photo of students working together in a classroom"></div>
  <div class="back-photo-boy" role="img" aria-label="Photo of a smiling boy at a school desk"></div>
  <h2 class="back-title">“Bridging Languages with Technology”</h2>
  <div class="back-panel">
    <p>Lingua Bridge Learning Partners offers consulting services and teacher training to schools and districts with emergent ESL populations, and/or growing second language programs.</p>
    <p>Pre- and in-service training sessions as well as consulting services are available both on-site and online. We take special pride in featuring open source (free) software programs for language learning and a hands-on approach to using the software effectively for both instruction and assessment.</p>
    <ul class="bullets">
      <li>Facilitating the acquisition of English for your LEP students</li>
      <li>Building second language programs for your LEP population</li>
      <li>On site in-service programs and videoconference workshops for faculty and staff</li>
      <li>Online consulting services for administration and teachers</li>
      <li>On site consulting for individuals or teams</li>
    </ul>
  </div>
  <div class="back-foot">
    <div class="brand"><span class="brand__dot"></span><span>Lingua Bridge<br>Learning Partners</span></div>
    <div class="web"><strong>www.linguabridgelearning.org</strong>1-555-014-2290 or 1-555-016-4471</div>
  </div>
</section>

<section class="card card--front" aria-label="Postcard front">
  <div class="front-photo" role="img" aria-label="Photo of a worried young girl sitting in a classroom chair"></div>
  <div class="front-copy">
    <p class="intro">Imagine what it’s like to be in a strange country and you don’t speak the language. Others stare at you, day in/ day out. You don’t know what they expect of you.</p>
    <p class="hook">. . . and you would do anything not to be in this chair . . . in this classroom . . . in this school.</p>
    <ul class="bullets">
      <li>Be the teacher, the school, the district to empower that child</li>
      <li>Broaden the learning experiences of all your students by engaging LEP students and their parents in your school community</li>
      <li>Improve or develop a language program worthy of a federal grant</li>
      <li class="shout">And do it all with the resources you already have!</li>
    </ul>
  </div>
  <div class="front-band">
    <div class="brand"><span class="brand__dot"></span><span>Lingua Bridge<br>Learning Partners</span></div>
    <div class="contact">PO Box 412 | Alder Creek, VA 20000-0412<br><strong>1-555-014-2290</strong> or <strong>1-555-016-4471</strong></div>
  </div>
</section>

</body>
</html>
```